To revamp/upgrade company website

We recently changed our company core values and mission statement, I have added this (very simply) via word press. However I would like the values and mission statement page design upgrading and also to have them run through the rest of the website pages. Also, open to other recommendations on how to update our website. The main take away from the website should be that we are the "people company", both for our customers and our staff. We would like the logo and colour theme to remain as is. Kestrand Healthcare is a health and social care company, who privately own a group of care homes in the north west of england. Attached is the core values, PEOPLE, our mission statement and also a word cloud that we would also like to embed in to the website.

```html
<!DOCTYPE html>
<html lang="en">
<head>
<meta charset="UTF-8">
<title>Kestrand Healthcare – The People Company</title>
<link href="https://fonts.googleapis.com/css2?family=Inter:wght@400;500;600;700;800&display=swap" rel="stylesheet">
<style>
:root{
  --navy:#36506f;
  --navy-dark:#2f4763;
  --peach:#e8997a;
  --peach-deep:#d4825f;
  --ink:#1d1d1f;
  --soft:#f5f5f5;
  --stage:#e9e9e9;
  --white:#ffffff;
}
*{box-sizing:border-box;margin:0;padding:0}
html,body{width:1200px;height:2869px;overflow:hidden}
body{background:var(--stage);font-family:'Inter',sans-serif;color:var(--ink)}
.page{position:absolute;left:50px;top:0;width:1100px;height:2869px;background:var(--white);overflow:hidden}
.abs{position:absolute}

/* header */
.site-header{left:0;top:0;width:1100px;height:57px;background:var(--white)}
.brand{left:14px;top:14px;display:flex;align-items:center;gap:8px;font-weight:700;font-size:22px;color:var(--navy);letter-spacing:.5px}
.brand-dot{width:16px;height:16px;border-radius:50%;background:var(--navy)}
.nav{right:18px;top:18px;display:flex;align-items:center;gap:27px;font-size:12px;color:var(--ink)}
.nav-cta{background:var(--navy);color:var(--white);font-weight:600;padding:5px 18px;clip-path:polygon(6% 0,100% 0,94% 100%,0 100%)}

/* hero */
.hero{left:0;top:57px;width:1100px;height:492px;background:linear-gradient(100deg,#4b5a5e 0%,#7c7c74 30%,#b9b2a8 55%,#d8d1c8 78%,#ece9e6 100%)}
.hero-title{left:51px;top:86px;font-size:54px;line-height:62px;font-weight:800;color:var(--white);letter-spacing:.3px}
.hero-sub{left:51px;top:218px;font-size:26px;line-height:35px;font-weight:400;color:var(--white);width:320px}
.hero-btn{left:51px;top:355px;width:216px;height:46px;background:var(--white);color:var(--navy);font-weight:700;font-size:21px;display:flex;align-items:center;justify-content:center;clip-path:polygon(8% 0,100% 0,92% 100%,0 100%)}
.hero-band{left:0;top:549px;width:1100px;height:8px}

/* values */
.values-title{left:0;top:626px;width:1100px;text-align:center;font-size:45px;font-weight:500;color:var(--navy)}
.values-title em{font-style:normal;color:var(--peach);font-weight:600}
.values-intro{left:0;top:688px;width:1100px;text-align:center;font-size:11.5px;line-height:13px}
.value{width:160px;text-align:center;font-size:11px;line-height:13px}
.value h3{color:var(--peach);font-size:16px;font-weight:600;margin-bottom:1px}
.value-shape{width:96px;height:110px}

/* feature rows */
.row-text{background:var(--soft);width:550px;height:344px}
.row-media{width:550px;height:344px}
.feature{width:260px}
.feature h2{font-size:30px;font-weight:600;color:var(--navy);margin-bottom:8px}
.feature p{font-size:14px;line-height:19px}
.btn{display:inline-flex;align-items:center;justify-content:center;background:var(--navy);color:var(--white);font-weight:600;font-size:15px;width:152px;height:36px;margin-top:18px;clip-path:polygon(10% 0,100% 0,90% 100%,0 100%);border-right:0}
.right{text-align:right}

/* home section */
.home-circle{left:157px;top:2212px;width:272px;height:272px;border-radius:50%;background:radial-gradient(circle at 45% 40%,#b4b4b4,#6f6f6f 70%,#4a4a4a)}
.home-halo{left:96px;top:2158px;width:400px;height:380px;border-radius:50%;background:#eef0f3}
.home-copy{left:542px;top:2262px;width:460px}
.home-copy h2{font-size:29px;font-weight:600;color:var(--navy);margin-bottom:12px}
.home-copy p{font-size:11.5px;line-height:19.5px;margin-bottom:19px}
.home-copy .btn{font-size:12px;width:112px;height:26px;margin-top:4px}

/* testimonials */
.reviews-title{left:120px;top:2622px;font-size:17px;font-weight:700}
.review{top:2659px;width:420px;height:137px;background:var(--soft);border-left:3px solid var(--navy);border-radius:4px;padding:18px 18px 0 18px;font-size:11px;line-height:18px}
.review cite{display:block;margin-top:9px;font-style:normal;font-weight:700;font-size:10.5px;color:var(--navy)}

.site-footer{left:0;top:2830px;width:1100px;height:39px;background:var(--navy);color:var(--white);font-size:10.5px;display:flex;align-items:center;justify-content:center}
</style>
</head>
<body>
<div class="page">

  <header class="site-header abs">
    <div class="brand abs"><span class="brand-dot"></span>Kestrand Healthcare</div>
    <nav class="nav abs">
      <span>Home</span><span>About Us</span><span>Live With Us</span><span>How We Care</span>
      <span>Help &amp; Support</span><span>Work With Us</span><span>FAQs</span>
      <span class="nav-cta">Contact Us</span>
    </nav>
  </header>

  <section class="hero abs" role="img" aria-label="Photo of a smiling elderly woman with a carer's hands on her shoulders">
    <h1 class="hero-title abs">PUTTING OUR<br>PEOPLE FIRST</h1>
    <p class="hero-sub abs">Creating a culture of excellence in delivering health care</p>
    <div class="hero-btn abs">GET IN TOUCH</div>
  </section>
  <svg class="hero-band abs" viewBox="0 0 1100 8" preserveAspectRatio="none">
    <rect x="0" y="0" width="1100" height="6" fill="#36506f"/>
    <rect x="0" y="0" width="520" height="3" fill="#e8997a"/>
  </svg>

  <h2 class="values-title abs">Our <em>PEOPLE</em> values</h2>
  <p class="values-intro abs">These values guide how we show up for residents, families, colleagues<br>and our community every day.</p>

  <svg width="0" height="0" style="position:absolute">
    <defs>
      <linearGradient id="peachFill" x1="0" y1="0" x2="0" y2="1">
        <stop offset="0" stop-color="#e39a7b"/><stop offset="1" stop-color="#cf7f5c"/>
      </linearGradient>
    </defs>
  </svg>

  <!-- upper labels -->
  <div class="value abs" style="left:258px;top:754px"><h3>Excellence</h3>We create an environment where residents and staff can thrive.</div>
  <div class="value abs" style="left:540px;top:754px"><h3>Passion</h3>We take pride in delivering exceptional care that makes a real difference.</div>
  <div class="value abs" style="left:820px;top:754px"><h3>Empathy</h3>We listen to understand the unique needs of others.</div>

  <!-- letter shapes -->
  <svg class="value-shape abs" style="left:149px;top:846px" viewBox="0 0 96 110"><polygon points="0,0 48,22 96,0 96,82 48,110 0,82" fill="url(#peachFill)"/><text x="48" y="70" text-anchor="middle" font-family="Inter,sans-serif" font-size="36" font-weight="600" fill="#fff">P</text></svg>
  <svg class="value-shape abs" style="left:290px;top:812px" viewBox="0 0 96 110"><polygon points="0,28 48,0 96,28 96,110 48,88 0,110" fill="url(#peachFill)"/><text x="48" y="68" text-anchor="middle" font-family="Inter,sans-serif" font-size="36" font-weight="600" fill="#fff">E</text></svg>
  <svg class="value-shape abs" style="left:431px;top:846px" viewBox="0 0 96 110"><polygon points="0,0 48,22 96,0 96,82 48,110 0,82" fill="url(#peachFill)"/><text x="48" y="70" text-anchor="middle" font-family="Inter,sans-serif" font-size="36" font-weight="600" fill="#fff">O</text></svg>
  <svg class="value-shape abs" style="left:572px;top:812px" viewBox="0 0 96 110"><polygon points="0,28 48,0 96,28 96,110 48,88 0,110" fill="url(#peachFill)"/><text x="48" y="68" text-anchor="middle" font-family="Inter,sans-serif" font-size="36" font-weight="600" fill="#fff">P</text></svg>
  <svg class="value-shape abs" style="left:712px;top:846px" viewBox="0 0 96 110"><polygon points="0,0 48,22 96,0 96,82 48,110 0,82" fill="url(#peachFill)"/><text x="48" y="70" text-anchor="middle" font-family="Inter,sans-serif" font-size="36" font-weight="600" fill="#fff">L</text></svg>
  <svg class="value-shape abs" style="left:852px;top:812px" viewBox="0 0 96 110"><polygon points="0,28 48,0 96,28 96,110 48,88 0,110" fill="url(#peachFill)"/><text x="48" y="68" text-anchor="middle" font-family="Inter,sans-serif" font-size="36" font-weight="600" fill="#fff">E</text></svg>

  <!-- lower labels -->
  <div class="value abs" style="left:117px;top:979px"><h3>Purpose</h3>We enrich lives and make a meaningful difference every day.</div>
  <div class="value abs" style="left:399px;top:979px"><h3>Openness</h3>We take pride in delivering exceptional care that makes a real difference.</div>
  <div class="value abs" style="left:680px;top:979px"><h3>Learning</h3>We grow through development, reflection and shared knowledge.</div>

  <!-- feature rows -->
  <div class="row-text abs" style="left:0;top:1097px"></div>
  <div class="feature abs" style="left:127px;top:1193px">
    <h2>TYPES OF CARE</h2>
    <p>We deliver tailored, individualised care in a “home from home” environment.</p>
    <span class="btn">Learn More</span>
  </div>
  <div class="row-media abs" style="left:550px;top:1097px;background:linear-gradient(120deg,#5f6f4d,#c9c2b6 45%,#6f93c4 80%,#c7c0ac)" role="img" aria-label="Photo of a nurse checking an elderly woman's blood pressure"></div>

  <div class="row-media abs" style="left:0;top:1441px;background:linear-gradient(135deg,#e6e3dc,#a9b0a8 40%,#7f8a86 60%,#d9d7ce)" role="img" aria-label="Photo of a stethoscope resting on banknotes"></div>
  <div class="row-text abs" style="left:550px;top:1441px"></div>
  <div class="feature right abs" style="left:700px;top:1537px;width:272px">
    <h2>Funding &amp; Support</h2>
    <p>Finding care for yourself or a loved one can be daunting – let our team guide you through the process.</p>
    <span class="btn">Learn More</span>
  </div>

  <div class="row-text abs" style="left:0;top:1785px"></div>
  <div class="feature abs" style="left:127px;top:1881px">
    <h2>Careers</h2>
    <p>We put our people first. Join a team that values, supports and invests in your growth.</p>
    <span class="btn">Learn More</span>
  </div>
  <div class="row-media abs" style="left:550px;top:1785px;background:linear-gradient(120deg,#d9dde2,#8aa5c8 35%,#eef0f2 60%,#7e9ccb)" role="img" aria-label="Photo of a smiling care worker with colleagues at a table"></div>

  <!-- home section -->
  <div class="home-halo abs"></div>
  <div class="home-circle abs" role="img" aria-label="Black and white photo of an elderly woman playing a keyboard"></div>
  <div class="home-copy abs">
    <h2>A Home from Home with Kestrand</h2>
    <p>At Kestrand Healthcare, we are dedicated to delivering personalised, one-to-one care tailored to each resident’s unique needs. Our goal is to create a true “home from home” where residents feel safe, respected and valued every day.</p>
    <p>Exceptional care starts with exceptional people. That’s why we invest in our teams, equipping them with the tools, training and compassion needed to provide truly person-centred support.</p>
    <span class="btn">Learn More</span>
  </div>

  <!-- testimonials -->
  <h2 class="reviews-title abs">What Our Families Say</h2>
  <blockquote class="review abs" style="left:120px">“My mum has been here for over two years. The home feels like a home and everyone – from care staff to office to cleaners – is friendly and helpful. Mum is very happy and says it’s the best place we could have picked for her.”<cite>– BB, Son of Resident</cite></blockquote>
  <blockquote class="review abs" style="left:560px">“My mother has dementia and mobility issues. The staff always include her in activities and have looked after her brilliantly. I cannot praise them highly enough.”<cite>– PC, Daughter of Resident</cite></blockquote>

  <footer class="site-footer abs">© 2025 Kestrand Healthcare. All rights reserved.</footer>
</div>
</body>
</html>
```